Simon & Lorna's Yuletide Unwind Bash

Invitation to a party 60-80 people at a private residence. Age range 30-40s.

Themes: summer/casual/Australian backyard/local community

**For delivery via both email and printed copy**
Would like one document suitable for both purposes or two versions for electronic or paper invitation. I will arrange printing so please prepare it in a suitable format.

Specimen text attached. Address and phone contact to follow by message with successful bidder

Thanks!
Simon

Target Market(s)

Locals, friends. Party attendees will typicaly be parents in their forties who who be leaving the kids at home for a relaxed party night, and walking home afterward

Industry/Entity Type

Community

Font styles to use
Sans Serif

Requirements
Should not have
• Cliche Australiana imagery. No kangaroos etc

```html
<!DOCTYPE html>
<html lang="en">
<head>
<meta charset="utf-8">
<title>Simon &amp; Lorna's Yuletide Unwind Bash – Details</title>
<link rel="stylesheet" href="https://fonts.googleapis.com/css2?family=Lato:wght@300;700&display=swap">
<style>
  :root {
    --bg: #000000;
    --heading: #ffffff;
    --body: #d4d4d4;
    --note: #c4c4c4;
    --rule: #9a9a9a;
  }
  html, body {
    margin: 0;
    padding: 0;
    background: var(--bg);
    overflow: hidden;
  }
  .invite-back {
    position: relative;
    width: 857px;
    height: 1200px;
    background: var(--bg);
    overflow: hidden;
    font-family: "Lato", Arial, sans-serif;
    color: var(--body);
  }
  .line {
    position: absolute;
    left: 0;
    width: 100%;
    margin: 0;
    text-align: center;
    white-space: nowrap;
  }
  .heading {
    font-weight: 700;
    font-size: 27px;
    line-height: 40px;
    color: var(--heading);
  }
  .detail {
    font-weight: 300;
    font-size: 26px;
    line-height: 40px;
    color: var(--body);
  }
  .text-us {
    font-weight: 300;
    font-size: 32px;
    line-height: 44px;
    color: var(--body);
  }
  .contacts {
    font-weight: 300;
    font-size: 27px;
    line-height: 40px;
    color: var(--body);
    word-spacing: 1px;
  }
  .rule {
    position: absolute;
    left: 135px;
    width: 583px;
    height: 1px;
    background: var(--rule);
  }
  .bring-friends {
    position: absolute;
    left: 0;
    width: 100%;
    top: 1003px;
    margin: 0;
    text-align: center;
    font-weight: 300;
    font-size: 24px;
    line-height: 30.5px;
    color: var(--note);
  }
  .phone-icon {
    position: absolute;
    left: 388px;
    top: 734px;
    width: 78px;
    height: 86px;
  }
</style>
</head>
<body>
  <main class="invite-back">
    <p class="line heading" style="top:152px">Child-free event</p>

    <p class="line heading" style="top:220px">DRESS</p>
    <p class="line detail" style="top:290px">summer casual, bare feet welcome</p>

    <p class="line heading" style="top:358px">Cocktail food provided</p>
    <p class="line detail" style="top:427px">BYO but only if you insist</p>

    <p class="line heading" style="top:495px">RSVP</p>
    <p class="line detail" style="top:564px">for catering would be nice.</p>

    <svg class="phone-icon" viewBox="0 0 78 86" aria-hidden="true">
      <rect x="3" y="3" width="38" height="62" rx="6" fill="none" stroke="#ffffff" stroke-width="5"/>
      <rect x="16" y="8" width="12" height="2.5" rx="1.2" fill="#ffffff"/>
      <circle cx="22" cy="58" r="3" fill="#ffffff"/>
      <path d="M41 30 C48 26 54 30 55 36 L60 46 C66 48 72 52 75 56 L62 84 L50 78 L38 70 C32 66 28 62 26 58 L41 58 Z" fill="#ffffff"/>
      <path d="M41 34 C46 32 50 35 50 40 L42 46 Z" fill="#000000"/>
    </svg>

    <p class="line text-us" style="top:834px">TEXT US before Xmas please.</p>
    <div class="rule" style="top:890px"></div>
    <p class="line contacts" style="top:910px">Simon |&nbsp; +971 000 24 61&nbsp; or&nbsp; Lorna | +971 000 24 61</p>
    <div class="rule" style="top:970px"></div>

    <p class="bring-friends">If you have some friends or neighbours that you like to<br>hang out with, we would love to meet.<br>Bring them with you!</p>
  </main>
</body>
</html>
```